TheKindFrame.net

TheKindFRame.net
Live World Art Gallery of pictures of love for all to enjoy
My goal is to create a website that is designed to be an online art gallery of photos that display what love looks like from all over the world. People will submit an image; write a short quote about why their image represents love
I Love THIS website:
http://peterwald.ca/
Please create something like this!!!
User Functionality:
Users must be able to do the following:
• Upload one photo
• Write a brief quote
• Share on their social media site
• Other users can like and share posted image
Backend:
• Site owner must be able to choose which images are uploaded. After user uploads image to site, admin will receive notice of the upload, and make sure the image is not unappropriated or spam. That would be the control functionality.
• At the bottom of the site a contact us, that will send e-mail to admin for any user related questions
Design Functionality:
Website should only be one, simple, elegant, page of photos.
Social Media:
Social media buttons should be small, at the corner of each submitted image
I Love THIS website:
http://peterwald.ca/
Homepage: I like the layout and design you have now. Each square/image will have the following social media options, friendlog,chirper,and Snapgrid. Below each photo their will be a caption that described each photo that appears after you hover over the photo, camera equipment, and a link to the photographer's portfolio/website. There will be able 30-40 images at a time on the homepage, 5-7 photographers at a time.
Featured Photographers:
This is the second page of the website. Here there is a bio of the photographers, how to contact them, and where in the world they are from. The photographers will always be on the page even after their work is taken off the homepage. I will insert links to their personal websites under their bio.
Review/Shop:
Here I will be using affiliated marketing to sell cameras, camera accessories, online photo classes, frames. I will not be selling the pictures featured on the homepage, people will be able to buy directly from the photographer.
Selling: I will be using rivora partners, and tap vault. I will be installing CoinDash, but all sales will be they third party vendors
Contact Us:
Here people can inquire about becoming a featured photographer, the company, and anything else
Site Requirements:
Email visitors can join the company mail group.
Target Market(s)
photographers, people who like snapgrid, and boardly
Industry/Entity Type
Marketing

```html
<!DOCTYPE html>
<html lang="en">
<head>
<meta charset="utf-8">
<title>The Kind Frame</title>
<link href="https://fonts.googleapis.com/css2?family=Open+Sans:ital,wght@0,300;0,400;0,600;1,400&display=swap" rel="stylesheet">
<style>
:root{
  --page:#e8e9ed;
  --white:#ffffff;
  --card:#f3f3f5;
  --ink:#555a60;
  --ink-soft:#8c9096;
  --line:#d6d8dc;
  --orange:#ff6d12;
  --green:#7fc31c;
  --icon:#a7abb0;
}
*{box-sizing:border-box;margin:0;padding:0}
html,body{width:960px;height:1200px;overflow:hidden}
body{background:var(--page);font-family:"Open Sans",Arial,sans-serif;color:var(--ink);position:relative}

.site-header{position:absolute;left:10px;top:0;width:931px;height:75px;background:var(--white);border-top:2px solid var(--line)}
.header-bar{height:46px;border-bottom:1px solid #e4e5e8;position:relative}
.menu-toggle{position:absolute;left:124px;top:15px;width:20px;height:14px;display:flex;flex-direction:column;justify-content:space-between}
.menu-toggle span{height:2px;background:#b5b8bd;border-radius:1px}
.search{position:absolute;left:158px;top:8px;width:160px;height:27px;border:1px solid #dfe0e3;border-radius:2px;display:flex;align-items:center;padding:0 10px;font-size:10.5px;color:#b3b6ba;justify-content:space-between}
.brand{position:absolute;left:0;right:0;top:6px;text-align:center;font-size:27px;font-weight:400;color:#3d4145;letter-spacing:.5px}
.logout{position:absolute;left:787px;top:15px}
.main-nav{display:flex;justify-content:center;gap:27px;padding-top:7px;font-size:10px;color:#50555a}

.hero{position:absolute;left:10px;top:75px;width:931px;height:280px;border-bottom:3px solid var(--orange);
  background:radial-gradient(ellipse at 20% 30%,#f7c66c 0%,#eea44a 35%,transparent 70%),
             radial-gradient(ellipse at 72% 55%,#e2352c 0%,#c9342a 18%,transparent 40%),
             linear-gradient(180deg,#f2b25a 0%,#e08d3c 55%,#b8632f 100%)}
.hero-caption{position:absolute;left:0;right:0;top:122px;text-align:center;color:var(--white);text-shadow:0 1px 3px rgba(0,0,0,.35)}
.hero-caption h1{font-size:30px;font-weight:400}
.hero-caption p{font-size:10.5px;margin-top:14px}
.hero-dots{position:absolute;left:0;right:0;top:255px;display:flex;justify-content:center;gap:8px}
.hero-dots span{width:10px;height:10px;border-radius:50%;background:rgba(255,255,255,.4)}
.hero-dots .active{background:var(--white)}
.hero-rule{position:absolute;left:10px;top:360px;width:931px;height:4px;background:var(--white)}

.gallery{position:absolute;left:44px;top:384px;display:flex;gap:9.6px}
.column{width:168px;display:flex;flex-direction:column;gap:8px}
.post{background:var(--card);border-radius:2px;overflow:hidden;box-shadow:0 1px 1px rgba(0,0,0,.05)}
.photo{display:block;width:100%}
.post-body{padding:14px 14px 13px}
.post-title{font-size:11.2px;font-weight:400;color:#4b5055;margin-bottom:7px}
.post-text{font-size:9.5px;line-height:12.8px;color:var(--ink-soft);font-weight:300}
.post-meta{display:flex;height:42px;background:var(--white)}
.post-meta div{flex:1;display:flex;align-items:center;justify-content:center;gap:8px;font-size:9.5px;color:#60656a}
.meta-comments{border-top:3px solid var(--orange);border-right:1px solid var(--line)}
.meta-date{border-top:3px solid var(--green)}

.quote{height:166px;padding:14px 14px 0;background:linear-gradient(160deg,#d9dadd,#e4e5e8 60%,#d2d3d7);position:relative}
.quote-mark{float:left;font-size:44px;line-height:34px;color:var(--white);margin-right:4px;font-family:Georgia,serif}
.quote p{font-style:italic;font-size:9.8px;line-height:15px;color:#6a6e73}
.quote cite{display:block;margin-top:7px;font-size:9.5px;color:#9a9ea3}

.site-footer{position:absolute;left:0;top:1152px;width:960px;height:48px;background:var(--orange);color:var(--white);font-size:9.5px;font-family:Arial,sans-serif;padding:19px 0 0 68px}
</style>
</head>
<body>

<header class="site-header">
  <div class="header-bar">
    <div class="menu-toggle"><span></span><span></span><span></span></div>
    <div class="search">Search
      <svg width="13" height="13" viewBox="0 0 13 13"><circle cx="5.5" cy="5.5" r="4.5" fill="none" stroke="#c2c5c9" stroke-width="1.2"/><line x1="9" y1="9" x2="12.5" y2="12.5" stroke="#c2c5c9" stroke-width="1.2"/></svg>
    </div>
    <div class="brand">The Kind Frame</div>
    <svg class="logout" width="18" height="16" viewBox="0 0 18 16"><path d="M6 1h10v14H6" fill="none" stroke="#b5b8bd" stroke-width="1.4"/><path d="M11 8H2M5 5L2 8l3 3" fill="none" stroke="#b5b8bd" stroke-width="1.4"/></svg>
  </div>
  <nav class="main-nav">
    <span>Portfolio</span><span>Celebrities</span><span>Commercial</span><span>404 Page</span><span>About</span><span>Contact Us</span>
  </nav>
</header>

<section class="hero" role="img" aria-label="Runner's red shoe on a sunlit track">
  <div class="hero-caption">
    <h1>Sport Equipment</h1>
    <p>Lorem Ipsum is simply dummy text of the printing simply dummy text of the printing</p>
  </div>
  <div class="hero-dots"><span></span><span></span><span></span><span></span><span class="active"></span><span></span></div>
</section>
<div class="hero-rule"></div>

<svg width="0" height="0" style="position:absolute">
  <defs>
    <symbol id="icon-comment" viewBox="0 0 18 16"><path d="M9 1.5c4.2 0 7.5 2.5 7.5 5.5S13.2 12.5 9 12.5c-.8 0-1.6-.1-2.3-.3L3 14.5l1-3.2C2.5 10.3 1.5 8.7 1.5 7 1.5 4 4.8 1.5 9 1.5z" fill="none" stroke="#a7abb0" stroke-width="1.2"/></symbol>
    <symbol id="icon-edit" viewBox="0 0 16 16"><path d="M13 9v6H1V3h6" fill="none" stroke="#a7abb0" stroke-width="1.2"/><path d="M6 10l1-3 6.5-6.5 2 2L9 9z" fill="none" stroke="#a7abb0" stroke-width="1.2"/></symbol>
  </defs>
</svg>

<main class="gallery">
  <div class="column">
    <article class="post">
      <div class="photo" style="height:150px;background:linear-gradient(160deg,#f3d2c9,#e7b5a8 60%,#d9a094)" role="img" aria-label="Close-up portrait of a baby"></div>
      <div class="post-body"><h2 class="post-title">Donec euismod fermentum</h2><p class="post-text">Donec euismod fermentum tellus, id congue purus tempor at. Fusce fringilla orci sit amet odio fermentum accumsan. Nam sed justo…</p></div>
      <div class="post-meta"><div class="meta-comments"><svg width="17" height="15"><use href="#icon-comment"/></svg>2</div><div class="meta-date"><svg width="15" height="15"><use href="#icon-edit"/></svg>12.02.14</div></div>
    </article>
    <article class="post">
      <div class="photo" style="height:234px;background:linear-gradient(160deg,#8d7a6a,#6c5a50 50%,#5a6c85)" role="img" aria-label="Portrait of a young woman in a denim shirt"></div>
      <div class="post-body"><h2 class="post-title">Donec euismod fermentum</h2><p class="post-text">Donec euismod fermentum tellus, id congue purus tempor at. Fusce fringilla orci sit amet odio fermentum accumsan. Nam sed justo…</p></div>
      <div class="post-meta"><div class="meta-comments"><svg width="17" height="15"><use href="#icon-comment"/></svg>2</div><div class="meta-date"><svg width="15" height="15"><use href="#icon-edit"/></svg>12.02.14</div></div>
    </article>
  </div>

  <div class="column">
    <article class="post">
      <div class="photo" style="height:206px;background:linear-gradient(180deg,#4d86d6,#a9c8ee 45%,#7fa448 65%,#5d8a2a)" role="img" aria-label="Green meadow with a tree under a blue sky"></div>
      <div class="post-body"><h2 class="post-title">Donec euismod fermentum</h2><p class="post-text">tellus, id congue purus tempor at. Fusce fringilla orci sit amet odio fermentum accumsan. Nam sed justo…</p></div>
      <div class="post-meta"><div class="meta-comments"><svg width="17" height="15"><use href="#icon-comment"/></svg>0</div><div class="meta-date"><svg width="15" height="15"><use href="#icon-edit"/></svg>12.02.14</div></div>
    </article>
    <article class="post">
      <div class="quote">
        <span class="quote-mark">“</span>
        <p>Lorem is not simply random text. It has roots in a piece of classical Latin literature from 45 BC, making it over 2000 years old. Tomas Verrell, a Latin professor at Corvell College in Ohio, looked up.</p>
        <cite>Arlen Westbrook</cite>
      </div>
      <div class="post-meta"><div class="meta-comments"><svg width="17" height="15"><use href="#icon-comment"/></svg>0</div><div class="meta-date"><svg width="15" height="15"><use href="#icon-edit"/></svg>12.02.14</div></div>
    </article>
  </div>

  <div class="column">
    <article class="post">
      <div class="photo" style="height:256px;background:linear-gradient(160deg,#5e4a3e,#a56a4a 45%,#d79a78 70%,#4a3a35)" role="img" aria-label="Portrait of a young woman with long brown hair"></div>
      <div class="post-body"><h2 class="post-title">Post Format: Standard</h2><p class="post-text">Donec euismod fermentum tellus, id congue purus tempor at. Fusce fringilla orci sit amet odio fermentum accumsan. Nam sed justo…</p></div>
      <div class="post-meta"><div class="meta-comments"><svg width="17" height="15"><use href="#icon-comment"/></svg>0</div><div class="meta-date"><svg width="15" height="15"><use href="#icon-edit"/></svg>23.05.14</div></div>
    </article>
    <article class="post">
      <div class="photo" style="height:152px;background:linear-gradient(160deg,#c9a48c,#e8c3a8 50%,#b88a70)" role="img" aria-label="Three fingertips drawn with smiling doodles"></div>
      <div class="post-body"><h2 class="post-title">Donec euismod fermentum</h2><p class="post-text">Donec euismod fermentum tellus, id congue purus tempor at. Fusce fringilla orci sit amet odio fermentum accumsan. Nam sed justo…</p></div>
      <div class="post-meta"><div class="meta-comments"><svg width="17" height="15"><use href="#icon-comment"/></svg>2</div><div class="meta-date"><svg width="15" height="15"><use href="#icon-edit"/></svg>12.02.14</div></div>
    </article>
  </div>

  <div class="column">
    <article class="post">
      <div class="photo" style="height:144px;background:linear-gradient(160deg,#6a6c6e,#3f4143 60%,#55575a)" role="img" aria-label="Dancer mid-leap against a grey wall"></div>
      <div class="post-body"><h2 class="post-title">Post Format: Audio</h2><p class="post-text">Donec euismod fermentum tellus, id congue purus tempor at. Fusce fringilla orci sit amet odio fermentum accumsan. Nam sed justo…</p></div>
      <div class="post-meta"><div class="meta-comments"><svg width="17" height="15"><use href="#icon-comment"/></svg>0</div><div class="meta-date"><svg width="15" height="15"><use href="#icon-edit"/></svg>23.05.14</div></div>
    </article>
    <article class="post">
      <div class="photo" style="height:251px;background:linear-gradient(160deg,#5a5d60,#2f3133 55%,#46494c)" role="img" aria-label="Dancer in motion on a dark backdrop"></div>
      <div class="post-meta"><div class="meta-comments"><svg width="17" height="15"><use href="#icon-comment"/></svg>0</div><div class="meta-date"><svg width="15" height="15"><use href="#icon-edit"/></svg>12.02.14</div></div>
    </article>
  </div>

  <div class="column">
    <article class="post">
      <div class="photo" style="height:103px;background:linear-gradient(180deg,#dfe6c8,#a9c46a 55%,#5f8a2a)" role="img" aria-label="Surreal green landscape with a balloon"></div>
      <div class="post-body"><h2 class="post-title">Post Format: Video</h2><p class="post-text">Donec euismod fermentum tellus, id congue purus tempor at. Fusce fringilla orci sit amet odio fermentum accumsan. Nam sed justo…</p></div>
      <div class="post-meta"><div class="meta-comments"><svg width="17" height="15"><use href="#icon-comment"/></svg>0</div><div class="meta-date"><svg width="15" height="15"><use href="#icon-edit"/></svg>23.05.14</div></div>
    </article>
    <article class="post">
      <div class="post-body"><p class="post-text">Donec euismod fermentum tellus, id congue purus tempor at. Fusce fringilla orci sit amet odio fermentum accumsan. Nam sed justo at felis tincidunt eleifend. Aliquam a dolor ut nibh placerat luctus ut a felis. Donec et imperdiet ipsum. Sed iaculis arcu sed neque mattis.</p></div>
      <div class="post-meta"><div class="meta-comments"><svg width="17" height="15"><use href="#icon-comment"/></svg>0</div><div class="meta-date"><svg width="15" height="15"><use href="#icon-edit"/></svg>12.02.14</div></div>
    </article>
    <article class="post">
      <div class="post-body"><h2 class="post-title">Donec euismod fermentum</h2><p class="post-text">Donec euismod fermentum tellus, id congue purus tempor at. Fusce fringilla orci sit amet odio fermentum accumsan. Nam sed justo…</p></div>
      <div class="post-meta"><div class="meta-comments"><svg width="17" height="15"><use href="#icon-comment"/></svg>2</div><div class="meta-date"><svg width="15" height="15"><use href="#icon-edit"/></svg>12.02.14</div></div>
    </article>
  </div>
</main>

<footer class="site-footer">2014 Copyright &copy; The Kind Frame</footer>

</body>
</html>
```